website in progress for new building development

Hi,
I have a new real estate development website in making but am running out of time for its completion. It's for a new apartment building for sales. Would it be possible for you to change/alter the site according to my requirements? I could send you all the existing files. The bulk of the website is done.
The images aren't really ready yet but will be within the next days so those will need to be replaced. Currently draft images are the placeholder on the website.

Let me know if you would be interested so we can quickly pick up correspondence.

This is the website so far (using Wordpress):
http://lindmoor.com.au/lindmoor/

Our domain is:
lindmoor.com.au

I am also adding the theme I am using.

Thanks.

Target Market(s)

Potential buyers.

Industry/Entity Type

Real Estate Development

Number of Pages Required

5+ page

Font styles to use
Other font styles liked:
• I used Robot under google fonts for the headlines

Requirements
Must have
• This is the current website
• http://lindmoor.com.au/lindmoor
• I'd like the colour scheme to remain the way it is.
• 1. Header
• I would like the header to have the menu on the right and have the 'Reigster' button similar to this website: (see the header here which shows up once you scroll down in the page) http://zenithbyfalconhouse.com.au/
• Please adjust this feature into our website with the menu items given.
• 2. Logo on Homepage
• Add the lindmoor logo into the top center of the feature image.
• Though permanent images are yet to arrive in the next few days. These are only drafts.
• 3. Footer
• Not sure about the colour scheme here yet.
• Should contain Disclaimer and copyrights.
• 4.Pages:
• a) Home
• b) Building
• c) Interior
• d) Location
• e) Register
• 5. page 'Home'
• When you scroll down in lindmoor.com.au/lindmoor/ you see the three images under the feature image, I would like those being hyperlinked as a 'box' just like this website has them when you scroll down here:
• http://www.velmotide.com.au/
• 6. page 'Register'
• I like the subtle colour scheme for the form used here http://zenithbyfalconhouse.com.au/#enquire-now
• and their 'Submit' button. Maybe adjust it to my website and remove the borders in the fields.
• 7. page 'Building'
• Will have two images of the exterior of the building which should be sliding automatically. (Images will be provided soon. For now I am only attaching draft images.)
• 8. page 'Interior'
• Will also have two images of the interior which should be automatically sliding. (Images will be provided soon. Attaching draft images for now)
Nice to have
• A language selection in the top right corner of each page:
• selection between english, mandarin, cantonese, korean.

```html
<!DOCTYPE html>
<html lang="en">
<head>
<meta charset="utf-8">
<title>Lindmoor — Contemporary Living</title>
<link rel="stylesheet" href="https://fonts.googleapis.com/css2?family=Josefin+Sans:wght@400;600;700&family=Roboto:wght@300;400;500&display=swap">
<style>
:root{
  --gold:#c8964a;
  --gold-dark:#b3813a;
  --sand:#f3e5cd;
  --ink:#3a3a3a;
  --muted:#6b6b6b;
  --white:#ffffff;
  --night:#111111;
}
*{box-sizing:border-box;margin:0;padding:0}
html,body{width:898px;height:1200px;overflow:hidden}
body{font-family:'Roboto',sans-serif;color:var(--ink);background:var(--white);position:relative}

.site-header{height:60px;display:flex;align-items:center;padding:0 30px;position:relative}
.brand{display:flex;align-items:center;gap:8px;font-family:'Josefin Sans',sans-serif;font-weight:600;font-size:15px;letter-spacing:2px;color:var(--gold)}
.brand-mark{width:18px;height:18px;background:var(--gold)}
.main-nav{position:absolute;left:324px;top:14px;display:flex;align-items:center}
.nav-item{font-size:11px;font-weight:500;letter-spacing:.5px;color:var(--ink);padding:0 15px;height:32px;line-height:32px;text-transform:uppercase}
.nav-item.is-active{background:var(--gold);color:var(--white);border-radius:16px;padding:0 28px;margin-right:10px}
.nav-register{position:absolute;left:688px;top:14px;width:152px;height:32px;border:1.5px solid var(--gold);border-radius:16px;text-align:center;line-height:30px;font-size:11px;font-weight:500;letter-spacing:.5px;color:var(--ink)}

.hero{position:relative;height:390px;background:linear-gradient(180deg,#d8dde2 0%,#c9c3bb 45%,#9a8c7d 78%,#6f6257 100%)}
.hero-arrow{position:absolute;top:252px;width:30px;height:30px;border-radius:50%;background:#1a1a1a;display:flex;align-items:center;justify-content:center}
.hero-arrow.prev{left:10px}
.hero-arrow.next{right:10px}

.intro{height:276px;background:var(--sand);text-align:center;padding-top:62px}
.intro-title{font-family:'Josefin Sans',sans-serif;font-weight:600;font-size:24px;letter-spacing:3px;color:var(--gold);text-transform:uppercase}
.intro-text{width:540px;margin:18px auto 0;font-size:12.5px;line-height:19px;color:var(--ink);font-weight:300}
.btn{display:inline-block;height:32px;line-height:30px;padding:0 22px;border-radius:16px;font-size:12px;border:1.5px solid var(--gold);color:var(--ink);background:var(--white)}
.intro .btn{margin-top:24px;background:transparent;color:var(--gold);padding:0 30px}
.btn.is-solid{background:var(--gold);color:var(--white)}

.features{display:flex;justify-content:space-between;padding:62px 45px 0;height:408px}
.feature{width:228px;text-align:center}
.feature-title{font-family:'Josefin Sans',sans-serif;font-weight:600;font-size:18px;letter-spacing:1.5px;color:var(--gold);text-transform:uppercase;height:30px}
.feature-photo{height:156px;margin-top:10px}
.photo-building{background:linear-gradient(180deg,#b9cde0 0%,#c89a84 55%,#7d6a5a 100%)}
.photo-interior{background:linear-gradient(180deg,#e9e6e1 0%,#c8b9a6 55%,#8b7a68 100%)}
.photo-location{background:linear-gradient(180deg,#c7dbec 0%,#d8cfc4 50%,#7f8f6c 100%)}
.feature-text{font-size:11px;line-height:15px;color:var(--muted);margin:16px auto 0;width:200px}
.feature .btn{margin-top:22px}

.site-footer{position:absolute;left:0;bottom:0;width:898px;height:66px;background:var(--night);display:flex;align-items:center;padding:0 40px}
.footer-brand{display:flex;align-items:center;gap:6px;font-family:'Josefin Sans',sans-serif;font-weight:600;font-size:11px;letter-spacing:1px;color:var(--gold)}
.footer-brand .brand-mark{width:10px;height:10px}
.copyright{font-size:11px;color:#cfcfcf;margin-left:8px}
.footer-nav{margin-left:auto;display:flex;align-items:center}
.footer-nav span{font-size:10px;color:#e5e5e5;padding:0 12px;text-transform:uppercase}
.footer-nav .is-active{border:1px solid #e5e5e5;border-radius:12px;height:24px;line-height:22px;padding:0 16px;margin-right:8px}
</style>
</head>
<body>
<header class="site-header">
  <div class="brand"><span class="brand-mark"></span>LINDMOOR</div>
  <nav class="main-nav">
    <span class="nav-item is-active">Home</span>
    <span class="nav-item">Building</span>
    <span class="nav-item">Interior</span>
    <span class="nav-item">Location</span>
  </nav>
  <span class="nav-register">REGISTER</span>
</header>

<section class="hero" role="img" aria-label="Bright apartment living room with white sofa and floor-to-ceiling windows overlooking the city">
  <span class="hero-arrow prev"><svg width="10" height="10" viewBox="0 0 10 10"><path d="M7 1 3 5l4 4" fill="none" stroke="#fff" stroke-width="2"/></svg></span>
  <span class="hero-arrow next"><svg width="10" height="10" viewBox="0 0 10 10"><path d="M3 1l4 4-4 4" fill="none" stroke="#fff" stroke-width="2"/></svg></span>
</section>

<section class="intro">
  <h1 class="intro-title">Contemporary Lindmoor Living</h1>
  <p class="intro-text">Located on a quiet suburban street, The Corvane is a striking and contemporary boutique development that opens up to the peace and tranquility of the great outdoors. Artfully conceived and expertly detailed, The Corvane is a distinctive and sculptural development of only 22 apartments, perfectly located beside lovely Harlow Beach.</p>
  <span class="btn">Read More</span>
</section>

<section class="features">
  <article class="feature">
    <h2 class="feature-title">Building</h2>
    <div class="feature-photo photo-building" role="img" aria-label="Exterior of the apartment building with balconies"></div>
    <p class="feature-text">Lorem ipsum dolor sit amet, consectetur adipiscing elit, sed do eiusmod tempor incididunt ut labore.</p>
    <span class="btn is-solid">View Building</span>
  </article>
  <article class="feature">
    <h2 class="feature-title">Interior</h2>
    <div class="feature-photo photo-interior" role="img" aria-label="Open-plan apartment interior with timber floors"></div>
    <p class="feature-text">Expertly detailed and perfectly appointed, each apartment is the result of a refined vision.</p>
    <span class="btn">View Interior</span>
  </article>
  <article class="feature">
    <h2 class="feature-title">Location</h2>
    <div class="feature-photo photo-location" role="img" aria-label="Street view of the building among trees"></div>
    <p class="feature-text">Lorem ipsum dolor sit amet, consectetur adipiscing elit, sed do eiusmod tempor incididunt ut labore.</p>
    <span class="btn">Our Location</span>
  </article>
</section>

<footer class="site-footer">
  <div class="footer-brand"><span class="brand-mark"></span>LINDMOOR</div>
  <span class="copyright">- 2015, All Rights Reserved.</span>
  <nav class="footer-nav">
    <span class="is-active">Home</span>
    <span>Building</span>
    <span>Interior</span>
    <span>Location</span>
  </nav>
</footer>
</body>
</html>
```